Zielgruppe
wir sind ein ambulanter Pflegedienst
Aufgabenstellung
Es soll ein Flyer entworfen werden.
Im Vordergrund steht die Behandlungspflege. Patienten sollen darauf aufmerksam gemacht werden, dass wir Insulininjektionen übernehmen und Kompressionsstrümpfe anziehen, wenn der Hausarzt dafür eine Verordnung ausstellt.
Im Vordergrund steht die Insulininjektion und das an und ausziehen der Kompressionsstrümpfe.
Falls die Patienten es nicht mehr alleine schaffen, springt der Pflegedienst ein.
Wichtig ist, dass das Pflegegeld nicht gekürzt wird, da dies eine Leistung der Krankenkasse ist.
Daten des Pflegedienstes:
Pflegehaus Lindental
Birkenweg 27
18057 Rostock
Tel 0800 4417236
www.Pflegehaus-Lindental.de
info@Pflegehaus-Lindental.de

```html
<!DOCTYPE html>
<html lang="de">
<head>
<meta charset="utf-8">
<title>Pflegehaus Lindental – Flyer Behandlungspflege</title>
<link rel="stylesheet" href="https://fonts.googleapis.com/css2?family=Fira+Sans:ital,wght@0,400;0,500;1,600&display=swap">
<style>
  :root {
    --green: #8dbf57;
    --blue: #2a3f8f;
    --blue-badge: #27529f;
    --white: #ffffff;
    --nurse-top: #8fd0da;
    --nurse-bottom: #f6f4f2;
  }
  * { margin: 0; padding: 0; box-sizing: border-box; }
  html, body { width: 1200px; height: 851px; overflow: hidden; background: var(--white); }
  .flyer {
    position: relative; width: 1200px; height: 851px; overflow: hidden;
    background: var(--white);
    font-family: "Fira Sans", sans-serif;
    color: var(--blue);
  }
  .brand { position: absolute; left: 30px; top: 22px; width: 220px; text-align: center; }
  .brand-ring {
    width: 153px; height: 153px; margin: 0 auto;
    border: 9px solid var(--blue); border-radius: 50%;
  }
  .brand-name {
    margin-top: 16px; font-size: 26px; font-weight: 500; line-height: 1.15;
    color: var(--green);
  }
  .headline {
    position: absolute; left: 254px; top: 52px;
    font-size: 58px; font-style: italic; font-weight: 600;
    color: var(--green); white-space: nowrap; letter-spacing: 0.5px;
    z-index: 2;
  }
  .swoosh { position: absolute; left: 284px; top: 138px; }
  .photo-nurse {
    position: absolute; left: 1010px; top: 22px; width: 190px; height: 580px;
    border-radius: 90px 90px 16px 16px;
    background: linear-gradient(180deg, #f7e6da 0%, var(--nurse-top) 25%, var(--nurse-top) 50%, var(--nurse-bottom) 62%, var(--nurse-bottom) 100%);
    opacity: 0.75;
  }
  .photo-round { position: absolute; border-radius: 50%; }
  .photo-insulin {
    left: 607px; top: 204px; width: 343px; height: 343px;
    border: 7px solid var(--blue);
    background: radial-gradient(circle at 45% 50%, #f6e1d3 0%, #f3dccd 45%, #fbf7f4 100%);
    z-index: 3;
  }
  .photo-stocking {
    left: 730px; top: 480px; width: 310px; height: 278px;
    border: 7px solid var(--green);
    background: radial-gradient(circle at 50% 50%, #efcdb6 0%, #eccab4 50%, #f8f1ec 100%);
    z-index: 2;
  }
  .question {
    position: absolute; left: 27px; top: 278px;
    font-size: 48px; font-style: italic; font-weight: 600; color: var(--green);
  }
  .services { position: absolute; left: 28px; top: 362px; }
  .services p {
    font-size: 31px; font-weight: 500; line-height: 51.5px;
    letter-spacing: -0.6px; white-space: nowrap; color: var(--blue);
  }
  .services .hl { color: var(--green); font-size: 33px; }
  .contact {
    position: absolute; left: 28px; top: 682px;
    font-size: 25.5px; font-weight: 400; line-height: 34px; color: var(--blue);
    white-space: nowrap;
  }
  .info-band {
    position: absolute; left: 0; top: 759px; width: 930px; height: 92px;
    background: var(--green); z-index: 4;
  }
  .info-band p {
    position: absolute; left: 29px; top: 22px;
    font-size: 37px; font-weight: 500; color: var(--white); white-space: nowrap;
    letter-spacing: -0.2px;
  }
  .cost-badge {
    position: absolute; left: 914px; top: 604px; width: 316px; height: 316px;
    border-radius: 50%; background: var(--blue-badge); z-index: 5;
  }
  .cost-badge p {
    position: absolute; left: 0; top: 78px; width: 302px; text-align: center;
    font-size: 32px; font-weight: 500; line-height: 41px; color: var(--white);
    letter-spacing: -0.9px;
  }
</style>
</head>
<body>
<div class="flyer">
  <div class="photo-nurse" role="img" aria-label="Lächelnde Pflegekraft in türkisfarbenem Kasack mit Stethoskop und Blutzuckermessgerät"></div>

  <div class="brand">
    <div class="brand-ring"></div>
    <div class="brand-name">Pflegehaus Lindental</div>
  </div>

  <h1 class="headline">Wir kümmern uns um Sie!</h1>
  <svg class="swoosh" width="616" height="50" viewBox="0 0 616 50" aria-hidden="true">
    <path d="M2 6 C 180 40, 380 54, 612 4 L 612 10 C 380 62, 180 48, 2 12 Z" fill="#2a3f8f"/>
  </svg>

  <div class="photo-round photo-insulin" role="img" aria-label="Blutzuckermessung mit Stechhilfe an der Fingerkuppe"></div>
  <div class="photo-round photo-stocking" role="img" aria-label="Anziehen eines Kompressionsstrumpfs am Fuß"></div>

  <h2 class="question">Benötigen Sie Hilfe?</h2>
  <div class="services">
    <p>Unser ambulantes Pflegeteam</p>
    <p>übernimmt auf ärztliche Verordnung</p>
    <p><span class="hl">Insulininjektionen</span> und</p>
    <p><span class="hl">Blutzuckerkontrollen</span> sowie das</p>
    <p><span class="hl">An- und Ausziehen von</span></p>
    <p><span class="hl">Kompressionsstrümpfen</span> für Sie!</p>
  </div>

  <div class="contact">
    <p>Pflegehaus Lindental • Birkenweg 27 • 18057 Rostock</p>
    <p>www.Pflegehaus-Lindental.de • info@Pflegehaus-Lindental.de</p>
  </div>

  <div class="info-band">
    <p>Informieren Sie sich kostenlos unter 0800 441 72 36</p>
  </div>

  <div class="cost-badge">
    <p>DIE KOSTEN<br>TRÄGT DIE<br>KRANKENKASSE</p>
  </div>
</div>
</body>
</html>
```